Korellas Einfühlungsvermögen in das Projekt, ihre Nachfragen an der richtigen Stelle und ihre frischen Ideen haben zu einem ebook-Cover geführt, mit dem ich sehr zufrieden bin. Die Kommunikation war sehr angenehm und professionell. Danke!
Zielgruppe
E-Book: Satirische Kurzgeschichten rund um Schule und Bildung.
Zielgruppe: Leute mit Humor und Interesse an einem Einblick ins Klassenzimmer einer jungen Berliner Lehrerin. Schüler, Eltern, Lehrer, Referendare...
Aufgabenstellung
Möglichst keine Comics mit Sprechblasen, eher stilvoll, intellektuell, trotzdem frisch, jung und modern.
Helle Farben, gerne Andeutungen der Themen Schule, Bildung, Unterricht.
Die Kurzgeschichten meines E-Books sind schnelle Momentaufnahmen, sie könnten auch als Blog erscheinen statt als Buch, evtl. lässt sich dies auch im Design widerspiegeln (?).

```html
<!DOCTYPE html>
<html lang="de">
<head>
<meta charset="utf-8">
<title>Kreide und Kaffee – Helga Prinz</title>
<link rel="stylesheet" href="https://fonts.googleapis.com/css2?family=Cormorant+Garamond:wght@500;600&family=IM+Fell+English&family=Tangerine:wght@400;700&display=swap">
<style>
  :root {
    --sky: #80d5f0;
    --sky-deep: #66c6e6;
    --dress-red: #b8303a;
    --label-white: #ffffff;
    --author-pink: #cf4a7e;
    --title-yellow: #fff64e;
    --subtitle-white: #ffffff;
  }
  html, body {
    margin: 0;
    padding: 0;
    overflow: hidden;
    background: #e9eef0;
  }
  .cover {
    position: relative;
    width: 750px;
    height: 1200px;
    overflow: hidden;
    background: var(--sky);
  }
  .cover-photo {
    position: absolute;
    inset: 0;
    background: linear-gradient(180deg, var(--sky) 0%, var(--sky-deep) 42%, #9a6a78 62%, var(--dress-red) 82%, var(--dress-red) 100%);
  }
  .author-label {
    position: absolute;
    left: 207px;
    top: 156px;
    width: 451px;
    height: 178px;
    background: var(--label-white);
    display: flex;
    align-items: center;
    justify-content: center;
  }
  .author-name {
    margin: 0;
    font-family: "Cormorant Garamond", "Times New Roman", serif;
    font-weight: 600;
    font-size: 50px;
    letter-spacing: 1px;
    color: var(--author-pink);
    text-transform: uppercase;
    line-height: 1;
  }
  .title {
    position: absolute;
    left: 0;
    top: 637px;
    width: 750px;
    margin: 0;
    font-family: "Tangerine", "Brush Script MT", cursive;
    font-weight: 700;
    font-size: 200px;
    line-height: 245px;
    color: var(--title-yellow);
    text-align: center;
    white-space: nowrap;
    text-shadow: 1px 2px 3px rgba(0,0,0,0.18);
  }
  .title-line { display: block; }
  .subtitle {
    position: absolute;
    left: 0;
    top: 1110px;
    width: 750px;
    margin: 0;
    font-family: "IM Fell English", "Georgia", serif;
    font-weight: 400;
    font-size: 54px;
    line-height: 1;
    color: var(--subtitle-white);
    text-align: center;
    white-space: nowrap;
    text-shadow: 1px 2px 3px rgba(0,0,0,0.35);
  }
</style>
</head>
<body>
  <main class="cover">
    <div class="cover-photo" role="img" aria-label="Platz für ein Foto: junge Lehrerin im roten Punktekleid vor hellblauem Hintergrund mit einem Stapel Bücher"></div>
    <div class="author-label">
      <p class="author-name">Helga Prinz</p>
    </div>
    <h1 class="title">
      <span class="title-line">Kreide und</span>
      <span class="title-line">Kaffee</span>
    </h1>
    <p class="subtitle">Notizen vom Lehrerpult</p>
  </main>
</body>
</html>
```